New Business Card Design Project VORASTI-Italy

we are VORASTI-Italy
our company in the market for 3 years we are luxury cosmetic company and its about time for a facelift :)
i will like to have elegant luxurious and unique business card
that will give the person that get it a unique, luxurious and elegant impression
I'm VERY OPEN FOR NEW IDEAS , even duo i add a few files of things that i see on line and i like them

i add my logo as well
my website is VORASTI.COM
(if you would like to see the main style that we have)

Target Market(s)

adult that have money :)

Industry/Entity Type

Business

Contact Information for Business Card

Name - Paul Vorasti
Position - CEO and CO Founder
address - 4817 E Larkdale
telephone - 555-384-1962
email - paul@vorasti.com
fax - 555-384-1962
website - VORASTI.COM

Colors
000000
959595
fbee3e
ffffff

Requirements
Must have
• big logo in GOLD color
• elegant look
• impressive
Nice to have
• not must but maybe classy pattern background
• not must but maybe emblem
• maybe clear plastic business card
Should not have
• colors
• images

```html
<!DOCTYPE html>
<html lang="en">
<head>
<meta charset="utf-8">
<title>VORASTI Italy – Business Card</title>
<link href="https://fonts.googleapis.com/css2?family=Bodoni+Moda:wght@500&family=Oswald:wght@600&family=Lato:wght@400&display=swap" rel="stylesheet">
<style>
  :root {
    --stage: #e9ecee;
    --ink: #2c2723;
    --ink-soft: #34302b;
    --gold-light: #e6c766;
    --gold: #c9a240;
    --gold-deep: #8e6a22;
    --gold-text: #d6b24e;
  }
  * { box-sizing: border-box; margin: 0; padding: 0; }
  html, body { width: 1200px; height: 900px; overflow: hidden; }
  body {
    background: var(--stage);
    display: flex;
    flex-direction: column;
    align-items: center;
    justify-content: center;
    gap: 40px;
  }
  .card {
    width: 700px;
    height: 400px;
    position: relative;
    overflow: hidden;
    box-shadow: 0 10px 30px rgba(0,0,0,.18);
  }

  /* Front */
  .card-front { display: flex; background: var(--ink); }
  .front-field {
    flex: 1;
    display: flex;
    align-items: center;
    justify-content: center;
    background: linear-gradient(135deg, var(--gold-light) 0%, var(--gold) 50%, var(--gold-deep) 100%);
  }
  .front-emblem {
    width: 210px;
    height: 210px;
    border: 4px solid var(--ink);
    border-radius: 50%;
    display: flex;
    align-items: center;
    justify-content: center;
    font-family: "Bodoni Moda", serif;
    font-weight: 500;
    font-size: 30px;
    letter-spacing: 3px;
    color: var(--ink);
  }
  .front-band {
    width: 170px;
    background: var(--ink);
    display: flex;
    align-items: center;
    justify-content: center;
  }
  .band-lockup {
    transform: rotate(90deg);
    text-align: center;
    color: var(--gold-text);
    font-family: "Bodoni Moda", serif;
    font-weight: 500;
    white-space: nowrap;
  }
  .band-rule { width: 250px; height: 3px; background: var(--gold-text); margin: 0 auto 10px; }
  .band-name { font-size: 50px; letter-spacing: 3px; line-height: 1; }
  .band-country { font-size: 15px; letter-spacing: 4px; margin-top: 10px; }

  /* Back */
  .card-back {
    display: flex;
    align-items: center;
    gap: 44px;
    padding: 0 60px;
    background: linear-gradient(135deg, var(--ink-soft), var(--ink));
  }
  .back-emblem {
    flex: none;
    width: 170px;
    height: 170px;
    border: 4px solid var(--gold-text);
    border-radius: 50%;
    display: flex;
    align-items: center;
    justify-content: center;
    font-family: "Bodoni Moda", serif;
    font-weight: 500;
    font-size: 24px;
    letter-spacing: 3px;
    color: var(--gold-text);
  }
  .back-details { color: var(--gold-text); }
  .person-name {
    font-family: "Oswald", sans-serif;
    font-weight: 600;
    font-size: 34px;
    letter-spacing: 1px;
    text-transform: uppercase;
    line-height: 1.1;
  }
  .person-role { font-family: "Lato", sans-serif; font-size: 17px; margin-top: 4px; }
  .contact-list { list-style: none; margin-top: 26px; font-family: "Lato", sans-serif; font-size: 15px; }
  .contact-list li { display: flex; align-items: center; gap: 12px; line-height: 1.9; }
  .contact-list li::before { content: ""; width: 8px; height: 8px; background: var(--gold-text); }
</style>
</head>
<body>
  <section class="card card-front" aria-label="Card front">
    <div class="front-field" role="img" aria-label="Gold background with fine diamond pattern and company emblem">
      <div class="front-emblem">VORASTI</div>
    </div>
    <div class="front-band">
      <div class="band-lockup">
        <div class="band-rule"></div>
        <div class="band-name">VORASTI</div>
        <div class="band-country">ITALY</div>
      </div>
    </div>
  </section>

  <section class="card card-back" aria-label="Card back" role="img">
    <div class="back-emblem">VORASTI</div>
    <div class="back-details">
      <h1 class="person-name">Paul Vorasti</h1>
      <p class="person-role">CEO and CO Founder</p>
      <ul class="contact-list">
        <li>555-384-1962</li>
        <li>555-384-1962</li>
        <li>paul@vorasti.com</li>
        <li>VORASTI.COM</li>
        <li>4817 E Larkdale</li>
      </ul>
    </div>
  </section>
</body>
</html>
```